Verin Subscription Infographic

I need an infographic to promote my new subscription service.
The infographic should be clear and consise, showcasing the benefits and the value of my offering.
I have provided a PDF that describes the service, and the offering in detail. I would like the designer to read the pdf document, understand the offering and design a one page infographic that will condense the information in a nice, visual way, to be shared within Brightlink for advertisment purposes.

```html
<!DOCTYPE html>
<html lang="en">
<head>
<meta charset="utf-8">
<title>Verin Subscription and Benefits</title>
<link href="https://fonts.googleapis.com/css2?family=Roboto:wght@300;400;500;700;900&family=Roboto+Condensed:wght@700&display=swap" rel="stylesheet">
<style>
:root{
  --backdrop:#403e52;
  --navy:#232b5e;
  --navy-2:#2f3a7a;
  --ink:#222;
  --muted:#555;
  --paper:#ffffff;
  --paper-soft:#f2f2f4;
  --sand:#c7ae86;
  --sand-deep:#8a7350;
  --sand-body:#e6d8c2;
  --silver:#e8e8ea;
  --silver-deep:#555;
  --gold:#f2b420;
  --gold-deep:#b98307;
  --gold-body:#fbe3a0;
  --graphite:#5a5a5e;
  --graphite-deep:#444;
  --violet:#8656c2;
  --violet-deep:#7a4fbf;
  --bar-yellow:#efbb38;
  --bar-green:#8cc63f;
  --bar-blue:#29aae1;
  --bar-orange:#f7931e;
}
*{box-sizing:border-box;margin:0;padding:0}
html,body{width:907px;height:1200px;overflow:hidden}
body{background:var(--backdrop);font-family:'Roboto',sans-serif;color:var(--ink);position:relative}
.panel{position:absolute;left:89px;width:730px;background:var(--paper)}
.pricing{top:84px;height:516px;background:linear-gradient(#f6f6f8,#fbfbfc 60%,#f4f4f6)}
.pricing-header{height:72px;background:var(--navy);position:relative}
.brand{position:absolute;left:48px;top:22px;display:flex;align-items:center;gap:6px;color:#fff;font-weight:700;font-size:22px;letter-spacing:.5px}
.brand-dot{width:24px;height:24px;border:2px solid #fff;border-radius:50%}
.pricing-title{position:absolute;left:197px;top:26px;font-family:'Roboto Condensed',sans-serif;font-size:26px;letter-spacing:4px;color:#fff}
.tier-backdrop{position:absolute;left:180px;top:96px;width:475px;height:268px;background:var(--navy)}
.tier{position:absolute;top:92px;width:119px;height:284px;border-radius:6px;border:1px solid #ddd;box-shadow:0 2px 6px rgba(0,0,0,.08)}
.tier-ribbon{position:absolute;left:12px;top:-12px;width:95px;height:50px;clip-path:polygon(0 0,100% 0,100% 62%,50% 100%,0 62%);font-family:'Roboto Condensed',sans-serif;font-size:15px;letter-spacing:1.5px;text-align:center;padding-top:12px;color:#fff}
.specs{position:absolute;top:50px;left:2px;right:2px}
.spec{display:flex;align-items:center;height:18px;padding-left:8px}
.spec:nth-child(odd){background:rgba(0,0,0,.04)}
.spec-label{font-size:5px;width:66px;color:#333}
.spec-value{font-size:9.5px;font-weight:700}
.spec-gap{height:17px;background:rgba(0,0,0,.04);margin-top:2px}
.features{position:absolute;top:151px;left:10px;right:4px;list-style:none}
.features li{display:flex;gap:5px;font-size:6.6px;line-height:8px;color:#333;margin-bottom:7px}
.features b{font-weight:700;color:#111;display:block}
.tick{flex:none;width:6px;height:6px;margin-top:1px}
.starter{left:49px;background:linear-gradient(#fff 38%,var(--sand-body))}
.starter .tier-ribbon{background:var(--sand)}
.starter .spec-value{color:var(--sand-deep)}
.starter .tick{fill:var(--sand)}
.entry{left:176px;background:linear-gradient(#fff 38%,var(--silver))}
.entry .tier-ribbon{background:linear-gradient(#f6f6f6,#e6e6e6);color:#111}
.entry .spec-value{color:var(--silver-deep)}
.entry .tick{fill:#bbb}
.member{left:302px;background:linear-gradient(#fff 38%,var(--gold-body));border-color:#f3cf6d}
.member .tier-ribbon{background:var(--gold)}
.member .spec-value{color:var(--gold-deep)}
.member .tick{fill:var(--gold)}
.premium{left:430px;background:linear-gradient(#fff 60%,#ddd);border-color:#999}
.premium .tier-ribbon{background:linear-gradient(#444,#9a9a9a)}
.premium .spec-value{color:var(--graphite-deep)}
.premium .tick{fill:var(--graphite)}
.exclusive{left:557px;background:linear-gradient(#fff 50%,#ece6f6);border-color:#b9a0dc}
.exclusive .tier-ribbon{background:linear-gradient(var(--violet),#c9b3e8)}
.exclusive .spec-value{color:var(--violet-deep)}
.exclusive .tick{fill:var(--violet)}
.fte-badge{position:absolute;left:26px;top:394px;width:112px;height:112px;border-radius:50%;background:radial-gradient(circle at 40% 35%,var(--navy-2),var(--navy));box-shadow:0 0 0 4px #fff,2px 3px 0 4px #c9cbe0;color:#fff;font-weight:700;font-size:11.5px;line-height:13.5px;text-align:center;display:flex;align-items:center;justify-content:center}
.support-list{position:absolute;left:152px;top:399px;width:202px;list-style:none}
.support-list li{font-size:6.6px;font-weight:500;color:#333;border-bottom:.7px solid var(--navy);padding:3px 0 3px;line-height:8px}
.support-list li:first-child{color:#777;font-weight:400}
.support-list li:first-child b{color:#333}
.support-rule{position:absolute;left:132px;top:394px}
.divider{position:absolute;left:377px;top:390px;height:118px;border-left:1px dashed #aaa}
.terms{position:absolute;left:395px;top:396px;width:285px}
.terms p{font-size:9.8px;font-weight:300;line-height:11.5px;color:#222;padding-bottom:6px;margin-bottom:6px;border-bottom:.7px solid #aaa}
.terms p:last-child{border:0}
.terms b{font-weight:700}
.team{top:609px;height:516px}
.team-title{position:absolute;top:30px;width:100%;text-align:center;font-family:'Roboto Condensed',sans-serif;font-size:24px;letter-spacing:2.6px;color:var(--navy)}
.lead-pill{position:absolute;left:242px;top:72px;width:252px;height:28px;border-radius:14px;background:linear-gradient(90deg,var(--navy),#3a5fbf);color:#fff;font-weight:700;font-size:10.5px;display:flex;align-items:center;justify-content:center}
.lead-note{position:absolute;top:116px;width:100%;text-align:center;font-size:11px;font-weight:300;line-height:12.5px}
.tree{position:absolute;left:0;top:0}
.role{position:absolute;top:186px;width:92px;text-align:center}
.role-name{font-size:6.8px;font-weight:700;line-height:8px;height:18px;color:#111}
.role-name span{font-weight:400}
.role-card{height:92px;background:var(--navy);border-radius:0 0 46px 46px;padding:7px 4px 0 8px;list-style:none;text-align:left}
.role-card li{display:flex;gap:3px;color:#fff;font-size:6.8px;font-weight:300;line-height:7.6px;padding:2px 0;border-bottom:.5px solid rgba(255,255,255,.25)}
.role-card li:last-child{border:0}
.role-card .tick{fill:#fff}
.usage{position:absolute;left:26px;top:325px;width:350px;height:172px;border:1px solid #e6e6e6;border-radius:8px}
.usage-title{text-align:center;font-weight:700;font-size:14px;line-height:16.5px;margin-top:8px;color:#111}
.usage-bars{position:absolute;left:8px;top:52px;width:306px;list-style:none}
.usage-bars li{position:relative;height:12px;border-radius:6px;background:var(--paper-soft);margin-bottom:6.7px}
.bar-fill{position:absolute;left:0;top:0;height:12px;border-radius:6px;color:#fff;font-size:7.5px;font-weight:700;text-align:right;padding-right:15px;line-height:12px}
.bar-name{position:absolute;right:16px;top:0;font-size:7px;line-height:12px;color:#333;letter-spacing:.3px}
.fill-yellow{background:var(--bar-yellow)}
.fill-green{background:var(--bar-green)}
.fill-blue{background:var(--bar-blue)}
.fill-orange{background:var(--bar-orange)}
.method{position:absolute;left:407px;top:360px;width:305px;font-size:12.6px;font-weight:300;line-height:14.6px}
.method b{font-weight:700}
.web{position:absolute;left:407px;top:465px;font-size:14px;letter-spacing:3.2px;color:#111}
</style>
</head>
<body>
<svg width="0" height="0" style="position:absolute">
  <symbol id="tick" viewBox="0 0 10 10"><circle cx="5" cy="5" r="5"/><path d="M2.8 5.2l1.6 1.6 3-3.3" fill="none" stroke="#fff" stroke-width="1.4"/></symbol>
</svg>

<section class="panel pricing">
  <header class="pricing-header">
    <div class="brand"><span class="brand-dot"></span>Verin</div>
    <h1 class="pricing-title">VERIN SUBSCRIPTION AND BENEFITS</h1>
  </header>
  <div class="tier-backdrop"></div>

  <article class="tier starter">
    <div class="tier-ribbon">STARTER</div>
    <div class="specs">
      <div class="spec"><span class="spec-label">Full Time Equivalent (FTE)</span><span class="spec-value">1 FTE</span></div>
      <div class="spec"><span class="spec-label">Price (Monthly)</span><span class="spec-value">£9,280</span></div>
      <div class="spec"><span class="spec-label">Engineering Hours Pool</span><span class="spec-value">160</span></div>
      <div class="spec"><span class="spec-label">Equivalent Hourly Price</span><span class="spec-value">£58</span></div>
      <div class="spec-gap"></div>
    </div>
    <ul class="features">
      <li><svg class="tick"><use href="#tick"/></svg><span>Online Support only</span></li>
      <li><svg class="tick"><use href="#tick"/></svg><span><b>Mainstream Tools</b>Emails accounts OfficeDesk PlanGantt</span></li>
    </ul>
  </article>

  <article class="tier entry">
    <div class="tier-ribbon">ENTRY</div>
    <div class="specs">
      <div class="spec"><span class="spec-label">Full Time Equivalent (FTE)</span><span class="spec-value">2 FTE</span></div>
      <div class="spec"><span class="spec-label">Price (Monthly)</span><span class="spec-value">£17,120</span></div>
      <div class="spec"><span class="spec-label">Engineering Hours Pool</span><span class="spec-value">320</span></div>
      <div class="spec"><span class="spec-label">Equivalent Hourly Price</span><span class="spec-value">£53.5</span></div>
      <div class="spec-gap"></div>
    </div>
    <ul class="features">
      <li><svg class="tick"><use href="#tick"/></svg><span>1 Engineer Semi-permanently on Site</span></li>
      <li><svg class="tick"><use href="#tick"/></svg><span><b>Mainstream Tools</b>Emails accounts OfficeDesk PlanGantt</span></li>
      <li><svg class="tick"><use href="#tick"/></svg><span>Relyo Verin In house Calculators</span></li>
    </ul>
  </article>

  <article class="tier member">
    <div class="tier-ribbon">MEMBER</div>
    <div class="specs">
      <div class="spec"><span class="spec-label">Full Time Equivalent (FTE)</span><span class="spec-value">3 FTE</span></div>
      <div class="spec"><span class="spec-label">Price (Monthly)</span><span class="spec-value">£24,900</span></div>
      <div class="spec"><span class="spec-label">Engineering Hours Pool</span><span class="spec-value">480</span></div>
      <div class="spec"><span class="spec-label">Equivalent Hourly Price</span><span class="spec-value">£51.9</span></div>
      <div class="spec-gap"></div>
    </div>
    <ul class="features">
      <li><svg class="tick"><use href="#tick"/></svg><span>Online Support only</span></li>
      <li><svg class="tick"><use href="#tick"/></svg><span><b>Mainstream Tools</b>Emails accounts OfficeDesk PlanGantt</span></li>
      <li><svg class="tick"><use href="#tick"/></svg><span>Relyo Verin In house Calculators</span></li>
      <li><svg class="tick"><use href="#tick"/></svg><span><b>Specialist Tools</b>Calcion SimFlow</span></li>
    </ul>
  </article>

  <article class="tier premium">
    <div class="tier-ribbon">PREMIUM</div>
    <div class="specs">
      <div class="spec"><span class="spec-label">Full Time Equivalent (FTE)</span><span class="spec-value">4 FTE</span></div>
      <div class="spec"><span class="spec-label">Price (Monthly)</span><span class="spec-value">£32,000</span></div>
      <div class="spec"><span class="spec-label">Engineering Hours Pool</span><span class="spec-value">640</span></div>
      <div class="spec"><span class="spec-label">Equivalent Hourly Price</span><span class="spec-value">£50</span></div>
      <div class="spec-gap"></div>
    </div>
    <ul class="features">
      <li><svg class="tick"><use href="#tick"/></svg><span>Online Support only</span></li>
      <li><svg class="tick"><use href="#tick"/></svg><span><b>Mainstream Tools</b>Emails accounts OfficeDesk PlanGantt</span></li>
      <li><svg class="tick"><use href="#tick"/></svg><span>Relyo Verin In house Calculators</span></li>
      <li><svg class="tick"><use href="#tick"/></svg><span><b>Specialist Tools</b>Calcion SimFlow</span></li>
      <li><svg class="tick"><use href="#tick"/></svg><span>High end software Motorix Anvera (Mech)</span></li>
    </ul>
  </article>

  <article class="tier exclusive">
    <div class="tier-ribbon">EXCLUSIVE</div>
    <div class="specs">
      <div class="spec"><span class="spec-label">Full Time Equivalent (FTE)</span><span class="spec-value">5 FTE</span></div>
      <div class="spec"><span class="spec-label">Price (Monthly)</span><span class="spec-value">£39,600</span></div>
      <div class="spec"><span class="spec-label">Engineering Hours Pool</span><span class="spec-value">600</span></div>
      <div class="spec"><span class="spec-label">Equivalent Hourly Price</span><span class="spec-value">£49.5</span></div>
      <div class="spec-gap"></div>
    </div>
    <ul class="features">
      <li><svg class="tick"><use href="#tick"/></svg><span>Online Support only</span></li>
      <li><svg class="tick"><use href="#tick"/></svg><span><b>Mainstream Tools</b>Emails accounts OfficeDesk PlanGantt</span></li>
      <li><svg class="tick"><use href="#tick"/></svg><span>Relyo Verin In house Calculators</span></li>
      <li><svg class="tick"><use href="#tick"/></svg><span><b>Specialist Tools</b>Calcion SimFlow</span></li>
      <li><svg class="tick"><use href="#tick"/></svg><span>High end software Motorix Anvera (Mech)</span></li>
      <li><svg class="tick"><use href="#tick"/></svg><span>Specialist Software Drivex MultiBody Dynamics</span></li>
    </ul>
  </article>

  <div class="fte-badge">See Subscription<br>Levels for FTE<br>Equivalent</div>
  <svg class="support-rule" width="22" height="112" viewBox="0 0 22 112"><path d="M0 20 L20 0 M0 92 L20 112" stroke="#232b5e" stroke-width=".7" fill="none"/></svg>
  <ul class="support-list">
    <li>Flexible Systems Engineering support including but not limited to: <b>MBSE, FMEA, requirements management and DVP creation</b></li>
    <li>Safety Engineer and DMFEA/Fault Tree Expert Support</li>
    <li>Project Manager and Engineering Management</li>
    <li>Power Electronics and Inverter Development Engineer Support</li>
    <li>Onsite Support (Hartwell)</li>
    <li>eMachine Design Engineer</li>
  </ul>
  <div class="divider"></div>
  <div class="terms">
    <p>Subscription Level can be <b>adjusted on a 3 month notice</b> (higher/lower number of FTE hours)</p>
    <p>If project needs increase, <b>upgrades on the service can be delivered potentially earlier</b>, pending Verin engineering team availability.</p>
    <p>If project needs are reduced, <b>with a 3 month notice we can reallocate the resources to other customers,</b> effectively being able to reduce the subscription service levels</p>
  </div>
</section>

<section class="panel team">
  <h2 class="team-title">VERIN AEROSPACE SYSTEMS ENGINEERING TEAM</h2>
  <div class="lead-pill">Team Leader &amp; Principal Project Manager</div>
  <p class="lead-note">Team Leadership - Task allocation and deliverables agreement<br>based on the level of the subscription service</p>
  <svg class="tree" width="730" height="190" viewBox="0 0 730 190">
    <g fill="none" stroke="#232b5e" stroke-width=".8">
      <path d="M368 100 V110 M368 138 V150 Q368 160 358 160 H78 Q70 160 70 168 V174 M368 150 Q368 160 378 160 H658 Q666 160 666 168 V174"/>
      <path d="M158 160 Q168 160 168 168 V174 M257 160 Q267 160 267 168 V174 M368 150 V174 M459 160 Q469 160 469 168 V174 M558 160 Q568 160 568 168 V174"/>
    </g>
    <g fill="#fff" stroke="#232b5e" stroke-width=".8">
      <circle cx="70" cy="177" r="3"/><circle cx="168" cy="177" r="3"/><circle cx="267" cy="177" r="3"/><circle cx="368" cy="177" r="3"/><circle cx="469" cy="177" r="3"/><circle cx="568" cy="177" r="3"/><circle cx="666" cy="177" r="3"/>
    </g>
  </svg>

  <div class="role" style="left:24px">
    <div class="role-name">Electric Motor Design Expert</div>
    <ul class="role-card">
      <li><svg class="tick"><use href="#tick"/></svg>Thermal analysis</li>
      <li><svg class="tick"><use href="#tick"/></svg>Electrical analysis</li>
      <li><svg class="tick"><use href="#tick"/></svg>Mechanical analysis</li>
      <li><svg class="tick"><use href="#tick"/></svg>CFD and Specialised</li>
      <li><svg class="tick"><use href="#tick"/></svg>Analysis Support</li>
    </ul>
  </div>
  <div class="role" style="left:122px">
    <div class="role-name">Requirements Engineer<br><span>(Based in Hartwell)</span></div>
    <ul class="role-card">
      <li><svg class="tick"><use href="#tick"/></svg>Requirements Management</li>
      <li><svg class="tick"><use href="#tick"/></svg>System Breakdown Analysis</li>
      <li><svg class="tick"><use href="#tick"/></svg>Boundary Diagrams</li>
      <li><svg class="tick"><use href="#tick"/></svg>Engineering Support</li>
    </ul>
  </div>
  <div class="role" style="left:221px">
    <div class="role-name">Requirements Engineer</div>
    <ul class="role-card">
      <li><svg class="tick"><use href="#tick"/></svg>Requirements Management</li>
      <li><svg class="tick"><use href="#tick"/></svg>System Breakdown Analysis</li>
      <li><svg class="tick"><use href="#tick"/></svg>Boundary Diagrams</li>
      <li><svg class="tick"><use href="#tick"/></svg>Engineering Support</li>
    </ul>
  </div>
  <div class="role" style="left:320px">
    <div class="role-name">Systems Safety and<br>DFMEA Expert</div>
    <ul class="role-card">
      <li><svg class="tick"><use href="#tick"/></svg>DFMEA</li>
      <li><svg class="tick"><use href="#tick"/></svg>FTA</li>
      <li><svg class="tick"><use href="#tick"/></svg>Flight Safety Assessement</li>
      <li><svg class="tick"><use href="#tick"/></svg>Support Safety Principles Engineering</li>
    </ul>
  </div>
  <div class="role" style="left:418px">
    <div class="role-name">Power Electronics and<br>Controls Engineer</div>
    <ul class="role-card">
      <li><svg class="tick"><use href="#tick"/></svg>Inverter HW Expertise</li>
      <li><svg class="tick"><use href="#tick"/></svg>Software Support</li>
      <li><svg class="tick"><use href="#tick"/></svg>Controls Engineering Development</li>
      <li><svg class="tick"><use href="#tick"/></svg>Leadership for Tier1</li>
    </ul>
  </div>
  <div class="role" style="left:516px">
    <div class="role-name">Test and Validation<br>Engineer</div>
    <ul class="role-card">
      <li><svg class="tick"><use href="#tick"/></svg>DVP Development</li>
      <li><svg class="tick"><use href="#tick"/></svg>DVP Execution Support</li>
      <li><svg class="tick"><use href="#tick"/></svg>Test Results Evaluation</li>
      <li><svg class="tick"><use href="#tick"/></svg>Test Robustness Validation</li>
    </ul>
  </div>
  <div class="role" style="left:615px">
    <div class="role-name">Mechanical Engineer</div>
    <ul class="role-card">
      <li><svg class="tick"><use href="#tick"/></svg>Mechanical Calculations</li>
      <li><svg class="tick"><use href="#tick"/></svg>Mechanical Designs and Drawings</li>
      <li><svg class="tick"><use href="#tick"/></svg>CAD Support</li>
      <li><svg class="tick"><use href="#tick"/></svg>Structural Analysis</li>
    </ul>
  </div>

  <div class="usage">
    <h3 class="usage-title">Utilization Needed Per Type of Engineer -<br>Sorted by Importance</h3>
    <ul class="usage-bars">
      <li><span class="bar-fill fill-yellow" style="width:160px">25%</span><span class="bar-name">Systems Engineering</span></li>
      <li><span class="bar-fill fill-green" style="width:143px">20%</span><span class="bar-name">Test &amp; Validation Engineering</span></li>
      <li><span class="bar-fill fill-green" style="width:143px">20%</span><span class="bar-name">Electronics and Control</span></li>
      <li><span class="bar-fill fill-blue" style="width:115px">15%</span><span class="bar-name">Mechanical Engineering</span></li>
      <li><span class="bar-fill fill-orange" style="width:84px">10%</span><span class="bar-name">System Safety</span></li>
      <li><span class="bar-fill fill-orange" style="width:84px">10%</span><span class="bar-name">Electric Motor Design</span></li>
    </ul>
  </div>

  <p class="method">In our proposed Engineering Subscription Service, the heart of its operation will be rooted in the <b>Agile project management methodology</b>. Every Monday, a focused alignment Sprint Design meeting will be set between our Project Manager and the Lead Customer Engineer from AeroNova .</p>
  <p class="web">www.verin-technology.co.uk</p>
</section>
</body>
</html>
```